Business Card Design Project

Please create a custom business card for Silverpine Golf Academy. The logo is attached to this brief.

Colours could be based on Blue, black, red, or white color. Colors like orange, green, purple, pink are not preferable.

Here is the link to the logo project : http://jobs.brieflantern.com/job.aspx?id=413057

Questions can be posted on the Discussion Board.

```html
<!DOCTYPE html>
<html lang="en">
<head>
<meta charset="utf-8">
<title>Silverpine Golf Academy – Business Card</title>
<link rel="stylesheet" href="https://fonts.googleapis.com/css2?family=Open+Sans:wght@400;600;700&display=swap">
<style>
  :root {
    --navy: #1c1f5e;
    --navy-deep: #14164a;
    --navy-light: #2a2f85;
    --ink: #1d1d2b;
    --paper: #ffffff;
    --backdrop: #e9e9ee;
  }
  * { margin: 0; padding: 0; box-sizing: border-box; }
  html, body {
    width: 1200px; height: 900px; overflow: hidden;
    background: var(--backdrop);
    font-family: "Open Sans", Arial, sans-serif;
  }
  .canvas { position: relative; width: 1200px; height: 900px; }

  .card {
    position: absolute;
    width: 560px; height: 320px;
    left: 320px;
    border-radius: 4px;
    overflow: hidden;
    box-shadow: 0 6px 18px rgba(20, 22, 74, 0.18);
  }

  /* Front: contact side */
  .card-front { top: 110px; background: var(--paper); color: var(--ink); }
  .contact { position: absolute; left: 34px; top: 30px; }
  .contact-name { font-size: 17px; font-weight: 600; letter-spacing: 0.5px; }
  .contact-title { font-size: 12px; color: var(--navy); margin-top: 1px; }
  .contact-address { font-size: 13px; line-height: 1.35; margin-top: 26px; }
  .contact-lines { list-style: none; margin-top: 10px; font-size: 13px; line-height: 1.4; }
  .contact-lines li { display: flex; align-items: center; gap: 8px; }
  .contact-lines svg { width: 11px; height: 11px; fill: var(--navy); flex: none; }

  .front-brand {
    position: absolute; right: 34px; top: 150px;
    display: flex; align-items: center; gap: 10px;
    color: var(--navy); font-weight: 700; font-size: 22px;
  }
  .brand-dot { width: 26px; height: 26px; border-radius: 50%; background: currentColor; flex: none; }

  .front-band { position: absolute; left: 0; bottom: 0; width: 560px; height: 72px; }
  .front-url {
    position: absolute; left: 34px; bottom: 14px;
    color: var(--paper); font-size: 14px; letter-spacing: 1.6px;
  }

  /* Back: brand side */
  .card-back {
    top: 470px;
    background: radial-gradient(ellipse at 55% 30%, var(--navy-light) 0%, var(--navy) 55%, var(--navy-deep) 100%);
    color: var(--paper);
  }
  .back-circle {
    position: absolute; left: 150px; top: -70px;
    width: 230px; height: 230px; border-radius: 50%;
    background: rgba(10, 12, 50, 0.35);
  }
  .back-brand {
    position: absolute; left: 0; right: 0; top: 178px;
    display: flex; justify-content: center; align-items: center; gap: 12px;
    font-weight: 700; font-size: 30px;
  }
  .back-brand .brand-dot { width: 34px; height: 34px; }
  .back-url {
    position: absolute; left: 0; right: 0; top: 240px;
    text-align: center; font-size: 15px; letter-spacing: 2.4px;
  }
</style>
</head>
<body>
<main class="canvas">

  <section class="card card-front" aria-label="Business card, contact side">
    <div class="contact">
      <p class="contact-name">MARK ELLISON</p>
      <p class="contact-title">Manager</p>
      <p class="contact-address">4120 Birch Hollow Rd<br>Cedar Park TX 78613</p>
      <ul class="contact-lines">
        <li>
          <svg viewBox="0 0 12 12" aria-hidden="true"><path d="M2.5 1l2 2.2-1 1.3a7 7 0 0 0 4 4l1.3-1 2.2 2-1.2 1.5C5 10.5 1.5 7 1 2.2z"/></svg>
          512 404 2270
        </li>
        <li>
          <svg viewBox="0 0 12 12" aria-hidden="true"><path d="M3.5 0h5a1 1 0 0 1 1 1v10a1 1 0 0 1-1 1h-5a1 1 0 0 1-1-1V1a1 1 0 0 1 1-1zm0 1.5v7.5h5V1.5z"/></svg>
          512 404 2271
        </li>
        <li>
          <svg viewBox="0 0 12 12" aria-hidden="true"><path d="M0 2.5h12v7H0zm1 .8v.3l5 3 5-3v-.3z"/></svg>
          info@SilverpineGolfAcademy.com
        </li>
      </ul>
    </div>

    <div class="front-brand">
      <span class="brand-dot" aria-hidden="true"></span>
      <span>Silverpine Golf Academy</span>
    </div>

    <svg class="front-band" viewBox="0 0 560 72" preserveAspectRatio="none" aria-hidden="true">
      <path d="M0 8 Q0 0 12 0 H360 Q380 0 385 22 Q390 44 410 44 H560 V72 H0 Z" fill="var(--navy)"/>
      <path d="M0 14 Q0 6 12 6 H355 Q372 6 378 26 Q385 50 410 50 H560 V72 H0 Z" fill="var(--navy-deep)" opacity="0.35"/>
    </svg>
    <p class="front-url">www.SilverpineGolfAcademy.com</p>
  </section>

  <section class="card card-back" aria-label="Business card, brand side">
    <div class="back-circle" aria-hidden="true"></div>
    <div class="back-brand">
      <span class="brand-dot" aria-hidden="true"></span>
      <span>Silverpine Golf Academy</span>
    </div>
    <p class="back-url">www.SilverpineGolfAcademy.com</p>
  </section>

</main>
</body>
</html>
```